Letterhead Design

We need a new Letterhead design for a 30 year old Electrical Company. We service domestic and commercial places. We have a logo recently made so to incorporate that. Using same colours or interested to see others added.
Would like to see a couple of options with all the info in letterhead, then another with info in a footnote down the bottom.

info needed to be added:

-Lic. No 48120
3/22-24 Tallow Rd, Kellbrook 2036
W - dorrickpower.com.au
T - (02) 9483 1720
M - 0437 592 816
E - info@dorrickpower.com.au
ABN: 41 729 504 316

```html
<!DOCTYPE html>
<html lang="en">
<head>
<meta charset="utf-8">
<title>Dorrick Power — Letterhead</title>
<link href="https://fonts.googleapis.com/css2?family=Josefin+Sans:wght@400;600&display=swap" rel="stylesheet">
<style>
  :root {
    --backdrop: #e6e7e8;
    --paper: #ffffff;
    --brand-orange: #f7992a;
    --brand-orange-soft: #fbd2a0;
    --brand-ink: #1f3434;
    --footer-ink: #2a2a2a;
  }
  * { margin: 0; padding: 0; box-sizing: border-box; }
  html, body {
    width: 1200px; height: 848px; overflow: hidden;
    background: var(--backdrop);
  }
  .canvas { position: relative; width: 1200px; height: 848px; }
  .letterhead {
    position: absolute; left: 400px; top: 131px;
    width: 400px; height: 566px;
    background: var(--paper);
    overflow: hidden;
    font-family: "Josefin Sans", sans-serif;
  }
  .brand-name {
    position: absolute; left: 32px; top: 54px;
    font-size: 21px; font-weight: 600;
    color: var(--brand-ink);
    letter-spacing: 0.2px;
    line-height: 1;
  }
  .footer-band {
    position: absolute; left: 0; bottom: 0;
    width: 400px; height: 94px;
    background: var(--brand-orange);
  }
  .bulb-decoration {
    position: absolute; right: 0; top: 354px;
    width: 48px; height: 170px;
    background: linear-gradient(180deg, var(--brand-orange-soft), #fde6c9);
    border-radius: 48px 0 0 20px;
    z-index: 2;
  }
  .contact-list {
    position: absolute; left: 19px; top: 12px;
    list-style: none;
    color: var(--footer-ink);
    font-size: 6.4px;
    font-weight: 400;
    line-height: 10px;
  }
  .contact-list .label { font-weight: 600; }
  .contact-list .strong { font-weight: 600; }
  .contact-list .fine { font-size: 5.2px; }
</style>
</head>
<body>
<main class="canvas">
  <section class="letterhead">
    <header class="brand-name">Dorrick Power</header>

    <footer class="footer-band">
      <ul class="contact-list">
        <li class="fine">Lic. No 48120</li>
        <li>3/22-24 Tallow Rd, Kellbrook 2036</li>
        <li class="strong">T (02) 9483 1720</li>
        <li class="strong">M 0437 592 816</li>
        <li><span class="label">E</span> info@dorrickpower.com.au</li>
        <li class="strong">www. dorrickpower.com.au</li>
        <li class="fine">ABN: 41 729 504 316</li>
      </ul>
    </footer>

    <div class="bulb-decoration" role="img" aria-label="Large orange outline light bulb decoration cropped at the page edge"></div>
  </section>
</main>
</body>
</html>
```